812 EDDM FLYER FOR CARPET CLEANING & WINDOW WASHING

Full Size Double Sided full color EDDM mailer

****PLEASE MAKE FONT TYPE, SIZE, COLOR, SPACING SAME AS IS EXAMPLE FLYER*******

***I have uploaded LOGO... It is on the VAN WRAP 812 CLEANING & RESTORATION

I have included an EDDM flyer and want my flyer to look like the example I uploaded.

I wanted to make it look Better & add my images and content. I have included the content under Must Haves......

Raindrop background

****Not all images will be used. Each service requires 2 images as seen on examply flyer... Please pic best 2 for each service, I can purchase new stock photo if needed

Target Market(s)

Residential Home Owners

Industry/Entity Type

Cleaning Service

Font styles to use
Serif

Colors
0555a3
ec1f27
fbed22
ffc214

Requirements
Must have
• Look Like Example EDDM postcard uploaded
• My images & content
• CARPET CLEANING Safe Eco-Friendly Truck Mounted Steam Cleaning. Say goodbye to those ugly carpet stains.
• WINDOW WASHING Interior/Exterior & Screens. Crystal Clear & Streak Free Windows
• POWER WASHING: Soft Wash & Power Wash. Safely cleans
• WATER DAMAGE: Got Mold or Water damage? Free IR Imaging Detection
• TILE & GROUT: Clean, Restore & Rejuvenate Tile, Grout & Stone
• MAINTENANCE: Professional & dependable repairs. We can Fit It!
• Call Today! 858-555-0147
• www.TidyNorth812.example
• ECO FRIENDLY CLEANING
• San Diego’s Trusted Cleaning Specialists

```html
<!DOCTYPE html>
<html lang="en">
<head>
<meta charset="utf-8">
<title>812 Eco Friendly Cleaning – EDDM Mailer</title>
<link href="https://fonts.googleapis.com/css2?family=Anton&family=Ubuntu:ital,wght@0,500;0,700;1,700&display=swap" rel="stylesheet">
<style>
  :root{
    --page:#ffffff;
    --brand-blue:#0555a3;
    --panel-blue:#0b52a2;
    --drop-blue-light:#3f86d6;
    --drop-blue-dark:#1c5cb3;
    --gold:#ffc214;
    --white:#ffffff;
  }
  *{box-sizing:border-box;margin:0;padding:0}
  html,body{width:1200px;height:1200px;overflow:hidden;background:var(--page)}
  .canvas{position:relative;width:1200px;height:1200px;background:var(--page)}

  .mailer{
    position:absolute;left:62px;top:196px;width:1077px;height:808px;
    overflow:hidden;
  }
  .raindrop-bg{
    position:absolute;inset:0;
    background:radial-gradient(ellipse at 50% 40%, var(--drop-blue-light), var(--drop-blue-dark));
  }

  .service-grid{
    position:absolute;left:44px;top:51px;width:982px;height:527px;
    display:grid;grid-template-columns:repeat(6,1fr);grid-template-rows:1fr 1fr;
    gap:3px;padding:3px;background:var(--gold);
    border-radius:24px;overflow:hidden;
  }
  .service-text{
    background:var(--panel-blue);color:var(--white);
    padding:12px 6px 0 11px;
    font-family:"Ubuntu",sans-serif;
  }
  .service-title{
    color:var(--gold);font-weight:700;font-size:27px;line-height:36px;
    height:74px;margin-bottom:4px;
  }
  .service-title.single{font-size:23px;line-height:30px;height:34px;margin-bottom:6px}
  .service-body{font-weight:700;font-size:15.5px;line-height:21px;white-space:nowrap}
  .service-tag{
    color:var(--gold);font-weight:700;font-style:italic;font-size:15.5px;line-height:21px;
    margin-top:7px;white-space:nowrap;
  }

  .photo{width:100%;height:100%}
  .photo-carpet{background:linear-gradient(180deg,#e9e5d6 0%,#d8d6cf 28%,#bfbcb6 100%)}
  .photo-window{background:linear-gradient(180deg,#2d79cf 0%,#5aa1e3 45%,#8a6a52 65%,#3f4a3a 100%)}
  .photo-power{background:linear-gradient(160deg,#6f8b4a 0%,#9bb07a 40%,#8a5a4a 75%,#b7a392 100%)}
  .photo-pipe{background:linear-gradient(135deg,#e8e6e0 0%,#a9a79f 50%,#6f6e69 100%)}
  .photo-framing{background:linear-gradient(180deg,#d9c4a0 0%,#efe6d6 45%,#c9b394 100%)}
  .photo-tile{background:linear-gradient(160deg,#8d8b85 0%,#b5b2aa 45%,#4a7fc4 60%,#9a9790 100%)}

  .badge-seal{
    position:absolute;left:46px;top:602px;width:246px;height:188px;
    background:var(--white);display:flex;align-items:center;justify-content:center;
  }
  .badge-seal .mark{width:172px;height:172px;border-radius:50%;background:#2aa7b5}
  .badge-cert{
    position:absolute;left:328px;top:690px;width:246px;height:98px;
    background:var(--white);display:flex;align-items:center;padding-left:6px;
  }
  .badge-cert .mark{width:82px;height:82px;border-radius:50%;background:#5cb85c}

  .headline,.web-address{position:absolute;overflow:visible}
  .headline{left:330px;top:600px;width:700px;height:80px}
  .web-address{left:600px;top:686px;width:429px;height:50px}
  .headline text,.web-address text{font-family:"Anton",sans-serif;fill:var(--gold)}

  .contact-line,.tagline{
    position:absolute;left:600px;width:429px;text-align:right;
    font-family:"Ubuntu",sans-serif;font-weight:700;white-space:nowrap;
  }
  .contact-line{top:740px;font-size:19px;line-height:24px;color:var(--white)}
  .contact-line .phone{color:var(--gold)}
  .tagline{top:766px;font-size:15.5px;line-height:21px;font-style:italic;color:var(--white)}
</style>
</head>
<body>
<div class="canvas">
  <section class="mailer">
    <div class="raindrop-bg" role="img" aria-label="Blue background covered in water droplets"></div>

    <div class="service-grid">
      <div class="photo photo-carpet" role="img" aria-label="Freshly steam cleaned carpet in a bright room with windows"></div>
      <div class="service-text">
        <h2 class="service-title">Carpet Cleaning</h2>
        <p class="service-body">Safe Eco-friendly<br>truck mounted<br>Steam Cleaning.</p>
        <p class="service-tag">Say Goodbye to<br>those ugly carpet<br>stains.</p>
      </div>
      <div class="photo photo-window" role="img" aria-label="Squeegee on a window overlooking rooftops and the ocean"></div>
      <div class="service-text">
        <h2 class="service-title">Window Washing</h2>
        <p class="service-body">Interior/Exterior &amp;<br>Screens</p>
        <p class="service-tag">Crystal Clear<br>&amp; Streak Free<br>Windows.</p>
      </div>
      <div class="photo photo-power" role="img" aria-label="Worker power washing a brick patio"></div>
      <div class="service-text">
        <h2 class="service-title">Power Washing</h2>
        <p class="service-body">Sort Wash &amp; Power<br>Wash.</p>
        <p class="service-tag">Safely Cleans.</p>
      </div>

      <div class="service-text">
        <h2 class="service-title">Water Damage</h2>
        <p class="service-body">Got Mold or Water<br>Damage?</p>
        <p class="service-tag">Free IR Imaging<br>Detection.</p>
      </div>
      <div class="photo photo-pipe" role="img" aria-label="Close-up of a leaking plumbing fitting over tile"></div>
      <div class="service-text">
        <h2 class="service-title single">Maintainance</h2>
        <p class="service-body">Professional<br>&amp; dependable<br>repairs.</p>
        <p class="service-tag">We can&nbsp; Fix it!</p>
      </div>
      <div class="photo photo-framing" role="img" aria-label="Room under repair with exposed wood framing and a step ladder"></div>
      <div class="service-text">
        <h2 class="service-title">Tile &amp; Grout</h2>
        <p class="service-body">Clean, Restore &amp;<br>Rejuvenate Tile,<br>Grout &amp; Stone.</p>
      </div>
      <div class="photo photo-tile" role="img" aria-label="Spinner tool cleaning stone tile flooring"></div>
    </div>

    <div class="badge-seal" role="img" aria-label="Certified products badge"><span class="mark"></span></div>
    <div class="badge-cert" role="img" aria-label="Cleaning certification badge"><span class="mark"></span></div>

    <svg class="headline" viewBox="0 0 700 80" aria-label="ECO FRIENDLY CLEANING">
      <text x="2" y="74" font-size="88" textLength="694" lengthAdjust="spacingAndGlyphs">ECO FRIENDLY CLEANING</text>
    </svg>
    <svg class="web-address" viewBox="0 0 429 50" aria-label="www.TidyNorth812.example">
      <text x="2" y="46" font-size="50" textLength="425" lengthAdjust="spacingAndGlyphs">www.TidyNorth812.example</text>
    </svg>
    <p class="contact-line">Call Today! <span class="phone">858-555-0147</span></p>
    <p class="tagline">San Diego’s Trusted Cleaning Specialists</p>
  </section>
</div>
</body>
</html>
```